Smart, Classy, Conservative looking Legal Letterhead

I need a letterhead that when you look at it it "says to you " this is a well established law firm with very smart lawyers, which will one day be appearing before the Grand Bench of the USA. All information about the Law firm should appear at the top of the page. please no information in the footer.

Legal

• The name of the law firm, both addresses, phone number and fax,, The names of the attorneys, the website.
• Fields that get changed such as the date, VIA, Address of who the letter is going to,
• Re, Index,
• should have a clean neat look, sleek
• some color would be nice. A logo of some sort could be nice as well. Maybe a single S or interlocking D's For Dorvik and Dorvik.
• not too modern looking.

```html
<!DOCTYPE html>
<html lang="en">
<head>
<meta charset="utf-8">
<title>Dorvik and Dorvik Law Firm — Letterhead</title>
<link rel="stylesheet" href="https://fonts.googleapis.com/css2?family=Roboto:wght@400;700;900&display=swap">
<style>
  :root {
    --canvas: #e9e9eb;
    --paper: #fbfbfc;
    --paper-edge: #dedfe2;
    --ink: #3b3c3f;
    --ink-soft: #6d6f74;
    --ink-faint: #b4b6bb;
    --accent: #9cc23f;
    --rule: #d9dadd;
  }
  * { box-sizing: border-box; margin: 0; padding: 0; }
  html, body { width: 1200px; height: 800px; overflow: hidden; }
  body {
    background: var(--canvas);
    font-family: "Roboto", Arial, sans-serif;
    color: var(--ink);
    position: relative;
  }
  .letterhead {
    position: absolute;
    left: 300px; top: 12px;
    width: 600px; height: 776px;
    background: linear-gradient(180deg, #f6f6f8 0%, var(--paper) 40%, #f3f3f5 100%);
    box-shadow: 0 2px 10px rgba(0,0,0,.12);
    border: 1px solid var(--paper-edge);
  }
  .abs { position: absolute; }

  /* brand */
  .brand { left: 40px; top: 110px; display: flex; align-items: center; gap: 8px; }
  .brand-square { width: 22px; height: 22px; background: var(--accent); }
  .brand-name { font-size: 11px; font-weight: 700; color: var(--accent); letter-spacing: .02em; }

  .firm-name {
    left: 168px; top: 62px;
    font-size: 15px; font-weight: 900; letter-spacing: .01em;
    text-transform: uppercase; color: var(--ink);
  }
  .recipient { left: 168px; top: 84px; font-size: 7.5px; line-height: 10.5px; color: var(--ink-soft); font-style: normal; }

  .label { font-size: 6.5px; font-weight: 700; text-transform: uppercase; color: var(--ink); letter-spacing: .03em; line-height: 9px; }
  .value { font-size: 7.5px; color: var(--ink-soft); line-height: 10.5px; }

  .contact-line { display: flex; align-items: center; gap: 5px; }
  .contact-line svg { width: 10px; height: 10px; flex: none; }

  .fax { left: 300px; top: 116px; }
  .reach { left: 168px; top: 146px; }
  .web { left: 300px; top: 157px; }
  .attorneys { left: 168px; top: 178px; }

  .divider { left: 420px; top: 62px; height: 140px; border-left: 1px dashed var(--rule); }
  .details { left: 434px; top: 62px; }
  .details .field { margin-bottom: 9px; }

  .accent-rule { height: 2px; background: var(--accent); }
  .top-rule { left: 0; width: 100%; top: 232px; }
  .mid-rule { left: 300px; width: 298px; top: 470px; height: 1px; background: linear-gradient(90deg, rgba(156,194,63,0) 0%, var(--accent) 60%); }
  .bottom-rule { left: 0; width: 100%; top: 700px; }

  .ref { left: 170px; font-size: 9px; font-weight: 700; color: var(--ink); display: flex; align-items: flex-end; gap: 6px; }
  .ref .blank { width: 240px; border-bottom: 1px dotted var(--ink-faint); height: 9px; }
  .ref-re { top: 258px; }
  .ref-index { top: 276px; }

  .letter-body { left: 200px; top: 336px; width: 290px; font-size: 8.5px; line-height: 12px; color: var(--ink-soft); }
  .letter-body p { margin-bottom: 9px; }
</style>
</head>
<body>
  <main class="letterhead">
    <div class="abs brand">
      <span class="brand-square"></span>
      <span class="brand-name">Dorvik &amp; Dorvik</span>
    </div>

    <h1 class="abs firm-name">Dorvik and Dorvik Law Firm</h1>
    <address class="abs recipient">
      Hon. Fake Judge Name Here<br>
      Grand Bench District Court, N.R.D.<br>
      200 Harbor Plaza<br>
      Courtroom 1042<br>
      Westbrook, NY 11590-3318
    </address>

    <div class="abs fax contact-line value">
      <svg viewBox="0 0 10 10" aria-hidden="true" fill="#6d6f74"><rect x="2.5" y="0.5" width="5" height="3"/><rect x="0.5" y="3.5" width="9" height="4" rx="1"/><rect x="2.5" y="7" width="5" height="2.5" fill="#fff" stroke="#6d6f74" stroke-width=".8"/></svg>
      <span>(555) 201-4479</span>
    </div>

    <div class="abs reach">
      <div class="label">Reach us @:</div>
      <div class="contact-line value">
        <svg viewBox="0 0 10 10" aria-hidden="true" fill="#6d6f74"><rect x="1" y="1" width="8" height="8" rx="1.5"/><rect x="3" y="3" width="4" height="2" fill="#fff"/></svg>
        <span>(555) 201-4478</span>
      </div>
    </div>

    <div class="abs web contact-line value">
      <svg viewBox="0 0 10 10" aria-hidden="true"><circle cx="5" cy="5" r="4.3" fill="none" stroke="#6d6f74" stroke-width="1"/><ellipse cx="5" cy="5" rx="1.8" ry="4.3" fill="none" stroke="#6d6f74" stroke-width=".8"/><line x1=".7" y1="5" x2="9.3" y2="5" stroke="#6d6f74" stroke-width=".8"/></svg>
      <span>www.dorvikdorvik.com</span>
    </div>

    <div class="abs attorneys">
      <div class="label">Attorneys:</div>
      <div class="value">Elias R. Dorvik<br>Nora J. Dorvik</div>
    </div>

    <div class="abs divider"></div>
    <div class="abs details">
      <div class="field"><div class="label">Date:</div><div class="value">July 4, 2015</div></div>
      <div class="field"><div class="label">Via:</div><div class="value">XXXXXXXX</div></div>
      <div class="field"><div class="label">Address:</div><div class="value">4810 Linden Road, Suite 2<br>Maple Grove, FL 32810</div></div>
    </div>

    <div class="abs accent-rule top-rule"></div>

    <div class="abs ref ref-re"><span>Re:</span><span class="blank"></span></div>
    <div class="abs ref ref-index"><span>Index:</span><span class="blank"></span></div>

    <section class="abs letter-body">
      <p>Your Honor:</p>
      <p>Pursuant to Your Honor's Individual Practices Rule III(C)(3), enclosed please find a courtesy copy of Plaintiff's Revised Yadda Yadda Yadda.</p>
      <p>Respectfully,</p>
      <p>Elias R. Dorvik</p>
    </section>

    <div class="abs mid-rule"></div>
    <div class="abs accent-rule bottom-rule"></div>
  </main>
</body>
</html>
```